Luxury Skincare Product Box Packaging Design

Vorabelle is a range of skincare products that help protect, nourish, and strengthen even the most sensitive skin, ensuring it is healthy, glowing, calm, and soft. Skincare practices support skin to enhance its appearance and relieve skin conditions. Your skin reflects your health. It is your body canvas and is an asset. The products contain naturally derived ingredients, aromatherapy oils, sustainable and ethical ingredients, organic ingredients where possible, natural preservatives and Australian oils, fruits, and extracts.

Vorabelle
Tagline is "Where Calm Finds Bloom"

Our products do not contain sulphates, parabens, phthalates, petrochemicals, synthetic colours, nor synthetic fragrances.

Everything about the Vorabelle Skincare name is creative and communicates luxury. Vorabelle from your first glance of the name, you will know that this is a company with excellent products.

By keeping it simple, unique, and elegant is often associated with high quality and is a way to establish trust. Vorabelle is a product that is “pure” and natural, so Vorabelle packaging would look simple, elegant, and clean.

I have uploaded the actual logo design and individual labels for the current skincare range I currently with the ingredients included so you can get an understanding of what I like. I have also added samples of package designs I quite like to assist with your designs.

Each Product box packaging sizes are as follows:

Product One - Exfoliating Herbs: 110mm (H) x 33mm Diameter
Product Two - Probiotic Lotion: 138mm (H) x 33mm Diameter
Product Three - Vitamin A Serum: 120mm (H) x 30mm Diameter
Updates

The Measurements are as follows: Product One: 110mm (H) x 33mm Diameter Product Two: 138mm (H) x 33mm Diameter Product Three: 120mm (H) x 30mm Diameter

Target Market(s)

Women

Requirements
Must have
• Logo, Product Name and ingredients and if you can barcode on the packaging that is the box design I am after
Nice to have
• samples of designs I like but open to suggestions

```html
<!DOCTYPE html>
<html lang="en">
<head>
<meta charset="utf-8">
<title>Vorabelle Probiotic Face Lotion – Box Dieline</title>
<link href="https://fonts.googleapis.com/css2?family=Montserrat:wght@300;400;600;700&display=swap" rel="stylesheet">
<style>
  :root{
    --paper:#ffffff;
    --blush:#fce6ef;
    --petal:#f3b6ca;
    --rose:#e98aa8;
    --cutline:#f0525c;
    --ink:#1d1d1d;
    --whisper:#9a9a9e;
    --rosegold:#b77e6a;
  }
  html,body{margin:0;padding:0;width:1200px;height:1200px;overflow:hidden;background:var(--paper);}
  .dieline{display:block;width:1200px;height:1200px;}
  .cut{fill:none;stroke:var(--cutline);stroke-width:1.3;}
  .panel-base{fill:var(--blush);}
  .copy{font-family:'Montserrat',sans-serif;fill:var(--ink);text-anchor:middle;font-size:14.5px;font-weight:400;}
  .copy .head{font-weight:700;}
  .caution{font-family:'Montserrat',sans-serif;fill:var(--ink);text-anchor:middle;font-size:12.5px;font-weight:700;}
  .caution-frame{fill:none;stroke:var(--ink);stroke-width:3;}
  .badge{fill:none;stroke:var(--rose);stroke-width:2;}
  .badge-label{font-family:'Montserrat',sans-serif;fill:var(--ink);text-anchor:middle;font-size:7px;font-weight:600;}
  .web{font-family:'Montserrat',sans-serif;fill:var(--ink);text-anchor:middle;font-size:15px;font-weight:700;}
  .tagline-word{font-family:'Montserrat',sans-serif;fill:var(--whisper);text-anchor:middle;font-size:18px;font-weight:400;letter-spacing:5px;}
  .brand-name{font-family:'Montserrat',sans-serif;fill:var(--rosegold);text-anchor:middle;font-size:72px;font-weight:300;letter-spacing:4px;}
  .product-name{font-family:'Montserrat',sans-serif;fill:#2c2c2c;font-size:31px;font-weight:300;letter-spacing:1px;}
  .skin-band{fill:var(--rosegold);}
  .skin-band-text{font-family:'Montserrat',sans-serif;fill:#fff;font-size:16px;font-weight:300;letter-spacing:1px;}
  .volume{font-family:'Montserrat',sans-serif;fill:var(--ink);font-size:14px;font-weight:400;}
</style>
</head>
<body>
<svg class="dieline" viewBox="0 0 1920 1920" xmlns="http://www.w3.org/2000/svg">
  <defs>
    <radialGradient id="wash-soft" cx="50%" cy="40%" r="75%">
      <stop offset="0" stop-color="#f7c6d6"/>
      <stop offset="1" stop-color="#fce8f0"/>
    </radialGradient>
    <radialGradient id="wash-deep" cx="65%" cy="72%" r="70%">
      <stop offset="0" stop-color="#eea0b9"/>
      <stop offset="0.55" stop-color="#f6cbd9"/>
      <stop offset="1" stop-color="#fce8f0"/>
    </radialGradient>
    <linearGradient id="wash-flap" x1="0" y1="0" x2="0" y2="1">
      <stop offset="0" stop-color="#f8d3df"/>
      <stop offset="1" stop-color="#f4bdcf"/>
    </linearGradient>
  </defs>

  <!-- watercolour wash areas -->
  <g class="watercolour" role="img" aria-label="Soft pink watercolour wash with faint botanical line drawing">
    <polygon points="413,452 475,421 475,1509 413,1478" fill="url(#wash-soft)"/>
    <rect x="475" y="421" width="261" height="1088" fill="url(#wash-soft)"/>
    <path d="M475,1509 H736 V1770 A130,95 0 0 1 475,1770 Z" fill="url(#wash-flap)"/>
    <polygon points="736,393 755,380 788,301 946,301 980,380 997,410 997,421 736,421" fill="var(--blush)"/>
    <rect x="736" y="421" width="261" height="1088" fill="url(#wash-soft)"/>
    <polygon points="736,1509 997,1509 997,1525 980,1538 946,1629 788,1629 750,1530" fill="var(--blush)"/>
    <path d="M997,160 V67 M997,160 A130,95 0 0 1 1257,160 V421 H997 Z" fill="url(#wash-flap)"/>
    <path d="M997,160 A130,93 0 0 1 1257,160 Z" fill="url(#wash-flap)"/>
    <rect x="997" y="421" width="260" height="1088" fill="url(#wash-deep)"/>
    <polygon points="1257,410 1275,385 1308,301 1467,301 1500,380 1518,393 1518,421 1257,421" fill="url(#wash-flap)"/>
    <rect x="1257" y="421" width="261" height="1088" fill="url(#wash-deep)"/>
    <polygon points="1257,1509 1518,1509 1518,1525 1500,1538 1467,1629 1308,1629 1275,1538 1257,1525" fill="url(#wash-flap)"/>
  </g>

  <!-- cut and fold lines -->
  <g class="cut">
    <polygon points="413,452 475,421 475,1509 413,1478"/>
    <rect x="475" y="421" width="261" height="1088"/>
    <path d="M475,1509 V1770 A130,95 0 0 0 736,1770 V1509"/>
    <line x1="475" y1="1770" x2="736" y2="1770"/>
    <polygon points="736,393 755,380 788,301 946,301 980,380 997,410 997,421 736,421"/>
    <rect x="736" y="421" width="261" height="1088"/>
    <polygon points="736,1509 997,1509 997,1525 980,1538 946,1629 788,1629 750,1530"/>
    <path d="M997,421 V160 A130,93 0 0 1 1257,160 V421"/>
    <line x1="997" y1="160" x2="1257" y2="160"/>
    <rect x="997" y="421" width="260" height="1088"/>
    <polygon points="1257,410 1275,385 1308,301 1467,301 1500,380 1518,393 1518,421 1257,421"/>
    <rect x="1257" y="421" width="261" height="1088"/>
    <polygon points="1257,1509 1518,1509 1518,1525 1500,1538 1467,1629 1308,1629 1275,1538 1257,1525"/>
  </g>

  <!-- back panel: product information -->
  <text class="copy">
    <tspan class="head" x="606" y="481">All Skin Types</tspan>
    <tspan x="606" y="499">Innovative moisturising</tspan>
    <tspan x="606" y="517">lotion soothes and settles</tspan>
    <tspan x="606" y="535">problematic and blemish</tspan>
    <tspan x="606" y="553">prone complexions.</tspan>
    <tspan x="606" y="589"><tspan class="head">Direction:</tspan> Apply a small</tspan>
    <tspan x="606" y="607">amount to your face</tspan>
    <tspan x="606" y="625">morning and night after</tspan>
    <tspan x="606" y="643">cleansing. Avoid eye area.</tspan>
    <tspan x="606" y="679"><tspan class="head">INGREDIENTS:</tspan> ALOE</tspan>
    <tspan x="606" y="697">BARBADENSIS (ALOE VERA)</tspan>
    <tspan x="606" y="715">LEAF JUICE, ROSA</tspan>
    <tspan x="606" y="733">EGLANTERIA (ROSEHIP) OIL*,</tspan>
    <tspan x="606" y="751">COCO- GLUCOSIDE, AGAVE</tspan>
    <tspan x="606" y="769">AMERICANA LEAF EXTRACT,</tspan>
    <tspan x="606" y="787">LACTOBACILLUS</tspan>
    <tspan x="606" y="805">BULGARICUS FERMENT</tspan>
    <tspan x="606" y="823">FILTRATE, EUCALYPTUS</tspan>
    <tspan x="606" y="841">GLOBULUS (TASMANIAN</tspan>
    <tspan x="606" y="859">BLUE GUM EXTRACT)</tspan>
    <tspan x="606" y="877">STEARIC ACID (VEGETABLE</tspan>
    <tspan x="606" y="895">DERIVED), GLYCERYL</tspan>
    <tspan x="606" y="913">STEARATE (VEGETABLE</tspan>
    <tspan x="606" y="931">DERIVED), GLYCERIN*,</tspan>
    <tspan x="606" y="949">CUCUMIS SATIVUS</tspan>
    <tspan x="606" y="967">(CUCUMBER) SEED OIL,</tspan>
    <tspan x="606" y="985">SALIX ALBA (WHITE</tspan>
    <tspan x="606" y="1003">WILLOW BARK), XANTHUS</tspan>
    <tspan x="606" y="1021">GUM, CETEARYL ALCOHOL</tspan>
    <tspan x="606" y="1039">(COCONUT DERIVED),</tspan>
    <tspan x="606" y="1057">TERIMINALIA ORIGANUM</tspan>
    <tspan x="606" y="1075">VULGARE OIL, THYMUS</tspan>
    <tspan x="606" y="1093">VULGARIS EXTRACT, OLEA</tspan>
    <tspan x="606" y="1111">EUROPEIA LEAF EXTRACT,</tspan>
    <tspan x="606" y="1129">ROSMARINUS OFFICINALIS</tspan>
    <tspan x="606" y="1147">LEAF EXTRACT, LAVANDULA</tspan>
    <tspan x="606" y="1165">ANGUSTIFOLIA (LAVENDER)</tspan>
    <tspan x="606" y="1183">FLOWER EXTRACT,</tspan>
    <tspan x="606" y="1201">PELARGONIUM</tspan>
    <tspan x="606" y="1219">GRAVEOLENS (GERANIUM) OIL</tspan>
    <tspan class="head" x="606" y="1239">*ORGANIC INGREDIENTS</tspan>
  </text>

  <rect class="caution-frame" x="505" y="1264" width="202" height="101"/>
  <text class="caution">
    <tspan x="606" y="1286">Store in a cool dry place</tspan>
    <tspan x="606" y="1303">Caution For external use</tspan>
    <tspan x="606" y="1320">only. Avoid contact with</tspan>
    <tspan x="606" y="1337">eyes. If irritation occurs,</tspan>
    <tspan x="606" y="1354">discontinue use.</tspan>
  </text>

  <g class="badges">
    <circle class="badge" cx="527" cy="1405" r="15"/>
    <circle class="badge" cx="566" cy="1405" r="15"/>
    <circle class="badge" cx="605" cy="1405" r="15"/>
    <circle class="badge" cx="645" cy="1405" r="15"/>
    <rect class="badge" x="671" y="1392" width="28" height="26" rx="3"/>
    <text class="badge-label"><tspan x="527" y="1431">Australian</tspan><tspan x="527" y="1439">Made</tspan></text>
    <text class="badge-label"><tspan x="566" y="1431">100%</tspan><tspan x="566" y="1439">Vegan</tspan></text>
    <text class="badge-label"><tspan x="605" y="1431">Cruelty</tspan><tspan x="605" y="1439">Free</tspan></text>
    <text class="badge-label"><tspan x="645" y="1431">Please</tspan><tspan x="645" y="1439">Recycle</tspan></text>
    <text class="badge-label"><tspan x="685" y="1431">6 months</tspan><tspan x="685" y="1439">once open</tspan></text>
  </g>

  <text class="web" x="606" y="1475">www.vorabelleskin.com</text>

  <!-- side panels: tagline -->
  <g class="tagline">
    <text class="tagline-word" x="866" y="692">Where</text>
    <text class="tagline-word" x="866" y="879">Calm</text>
    <text class="tagline-word" x="866" y="1066">Finds</text>
    <text class="tagline-word" x="866" y="1252">Bloom</text>
    <text class="tagline-word" x="1387" y="692">Where</text>
    <text class="tagline-word" x="1387" y="879">Calm</text>
    <text class="tagline-word" x="1387" y="1066">Finds</text>
    <text class="tagline-word" x="1387" y="1252">Bloom</text>
  </g>

  <!-- front panel -->
  <text class="brand-name" transform="translate(1140,740) rotate(-90)">Vorabelle</text>

  <text class="product-name">
    <tspan x="1026" y="1143">PROBIOTIC</tspan>
    <tspan x="1026" y="1180">FACE</tspan>
    <tspan x="1026" y="1215">LOTION</tspan>
  </text>
  <rect class="skin-band" x="1025" y="1238" width="169" height="26"/>
  <text class="skin-band-text" x="1034" y="1257">ALL SKIN TYPES</text>

  <text class="volume" x="1025" y="1480">40 ml</text>
</svg>
</body>
</html>
```